Zielgruppe
Unternehmensberater, Spezialbereiche Sales und Recruiting
Arbeiten mit der Kaskadal Methode
Zielgruppe sind Führungskräfte in der HR- oder Sales-Abteilung
Management consultant, specialising in sales and recruiting
Working with the Kaskadal Method
Target group are managers in the HR or sales department
Aufgabenstellung
Bitte keine Magneten, Zielscheiben, Schiffe etc. Das kommt so oft vor. Es geht um Touchpoints, die aufeinander abgestimmt sind. Wertigkeit, kreative und besondere Dinge.
Buchtitel (NEU!!!!!)
(Autorin) Marlene Vogtherr
(Subtitel aber darüber) Brisk Lane Closing (BLC®)
(Haupttitel) Mit Schwung, Klarheit und Ideenreichtum zu Ihrem Traumauftrag.
(Subtitel 2) Alltagsbewährte Kniffe für Ihren Abschlussgewinn (im Kreis)
– siehe Layout unten das wir für einen anderen Titel schon gemacht hatten –
Format: DIN A6, Taschenguide. Schnell zur Hand und schnell gelesen.
Please no magnets, targets, ships, etc. That happens so often. It's about touchpoints that are coordinated. Value, creative and special things.
Book title (NEW!!!!!)
(Author) Marlene Vogtherr
(Subtitle but above) Brisk Lane Closing (BLC®)
(Main title) With verve, clarity and inventiveness to your dream client.
(Subtitle 2) Tested tricks for your closing gains (in a circle)
- see layout below which we had already done for another title -
Format: DIN A6, pocket guide. Quickly to hand and quickly read.
Translated with www.Ubrivo.com/Converter (free version)

```html
<!DOCTYPE html>
<html lang="de">
<head>
<meta charset="utf-8">
<title>Brisk Lane Closing – Buchcover</title>
<link rel="stylesheet" href="https://fonts.googleapis.com/css2?family=Roboto+Condensed:wght@400;700&family=Roboto:wght@400&display=swap">
<style>
  :root {
    --stage: #ece9e6;
    --cover: #dfe0ea;
    --ink: #6c6c70;
    --tab: #808084;
    --white: #ffffff;
    --badge: #ab8bb9;
    --pastel-pink: #f0b8c6;
    --pastel-blue: #9fb0d4;
    --pastel-orange: #f3c996;
    --pastel-teal: #a7d7dc;
  }
  * { margin: 0; padding: 0; box-sizing: border-box; }
  html, body {
    width: 1200px; height: 900px; overflow: hidden;
    background: var(--stage);
  }
  .book-cover {
    position: absolute;
    left: 310px; top: 39px;
    width: 580px; height: 822px;
    background: var(--cover);
    overflow: hidden;
    font-family: "Roboto Condensed", "Arial Narrow", sans-serif;
    color: var(--ink);
  }
  .author-tab {
    position: absolute;
    left: 173px; top: 0;
    width: 209px; height: 41px;
    background: var(--tab);
    border-radius: 0 0 12px 12px;
    color: var(--white);
    font-family: "Roboto", Arial, sans-serif;
    font-size: 16px;
    line-height: 41px;
    text-align: center;
    text-transform: uppercase;
  }
  .series-title {
    position: absolute;
    left: 0; right: 0; top: 52px;
    text-align: center;
    font-weight: 700;
    font-size: 29px;
    letter-spacing: 0.2px;
    text-transform: uppercase;
  }
  .cover-illustration {
    position: absolute;
    left: 0; top: 92px;
    width: 580px; height: 450px;
    background:
      radial-gradient(circle at 38% 30%, var(--pastel-pink) 0, transparent 22%),
      radial-gradient(circle at 64% 34%, var(--pastel-blue) 0, transparent 22%),
      radial-gradient(circle at 38% 64%, var(--pastel-orange) 0, transparent 22%),
      radial-gradient(circle at 62% 66%, var(--pastel-teal) 0, transparent 22%),
      var(--cover);
  }
  .main-title {
    position: absolute;
    left: 56px; top: 548px;
    font-weight: 700;
    font-size: 46px;
    line-height: 44px;
    text-transform: uppercase;
  }
  .tips-badge {
    position: absolute;
    left: 371px; top: 590px;
    width: 180px; height: 180px;
  }
  .tips-badge svg { position: absolute; inset: 0; }
  .tips-badge-text {
    position: absolute;
    inset: 0;
    display: flex; align-items: center; justify-content: center;
    transform: rotate(-20deg);
    color: var(--white);
    font-weight: 700;
    font-size: 14.5px;
    line-height: 17px;
    text-align: center;
    text-transform: uppercase;
  }
</style>
</head>
<body>
  <main class="book-cover">
    <div class="author-tab">Marlene Vogtherr</div>
    <h2 class="series-title">Brisk Lane Closing (BLC®)</h2>
    <div class="cover-illustration" role="img" aria-label="Illustration: vier Hände fügen pastellfarbene Puzzleteile in Rosa, Blau, Orange und Türkis zusammen"></div>
    <h1 class="main-title">Mit Schwung,<br>Klarheit und<br>Ideenreichtum<br>zu Ihrem<br>Traumauftrag.</h1>
    <div class="tips-badge">
      <svg viewBox="0 0 180 180" aria-hidden="true">
        <rect x="25" y="25" width="130" height="130" rx="22" fill="var(--badge)" transform="rotate(-20 90 90)"/>
      </svg>
      <p class="tips-badge-text">Alltagsbewährte<br>Kniffe für Ihren<br>Abschlussgewinn</p>
    </div>
  </main>
</body>
</html>
```